UX interface for a Crypto currency payment gateway

This project requires you to open an account on our development web site http://dev.vorplin.com/cgi-bin/d

It requires you, as well, to download and install a Bitcoin client working on the testnet network (such as electrum), then get some Bitcoin testnet (those are free for who knows how to get them). "Simulate a payment" works as well.

This project requires you to know how to work with Bitcoins and cryptocurrencies.

Do NOT submit work if you're not interested in crypto-currencies.

Then, make some simulated payments on our development web site (Bitcoin testnet is only one supported crypto-currency there) to fill up a little bit the transaction report and the wallets.

Our UX sucks, yep, I know that, that's why we need you !

Then propose a design for the back office, first page is good enough (Accounts & Wallets).

You can change the layout as you see fit, the contest is as much about the UX design than the graphic design.

The price of the contest is for the best design of the first page only (Accounts & Wallets).

However, the winner will be required to code his design in HTML/CSS (JS may be required as well depending on your design) and he will get the whole back office and check out page to design and code in a one to one relationship with the customer (be prepared for a long term project). The winner will integrate his coding inside our templates.

Do NOT submit work if you're not interested to take the whole project or if you're not able to dedicate enough time to deliver a big quantity of work fast.
Updates

Requirements
Must have
• Design must look professional in "bank" style.

```html
<!DOCTYPE html>
<html lang="en">
<head>
<meta charset="utf-8">
<title>Orvelle Ledger – Accounts &amp; Wallet</title>
<link href="https://fonts.googleapis.com/css2?family=Poppins:wght@400;500&display=swap" rel="stylesheet">
<style>
:root{
  --green:#1fbf36;
  --green-dark:#1a8f2a;
  --page:#f2f2f2;
  --white:#ffffff;
  --panel:#f3f3f3;
  --ink:#1e1e1e;
  --ink-soft:#333333;
  --line:#d9d9d9;
  --stripe:#f0f0f0;
}
*{box-sizing:border-box;margin:0;padding:0}
html,body{width:1200px;height:1086px;overflow:hidden}
body{background:var(--page);font-family:'Poppins',sans-serif;color:var(--ink);position:relative}
.topbar{position:absolute;left:0;top:0;width:1200px;height:94px;background:var(--white)}
.brand{position:absolute;left:56px;top:40px;display:flex;align-items:center;gap:8px;font-size:21px;font-weight:500;color:var(--ink);white-space:nowrap}
.brand-dot{width:16px;height:16px;border-radius:50%;background:var(--green);flex:none}
.top-icons{position:absolute;left:1035px;top:33px;display:flex;gap:13px}
.icon-btn{width:30px;height:30px;border:1px solid #8a8a8a;border-radius:50%;display:flex;align-items:center;justify-content:center}
.navband{position:absolute;left:0;top:94px;width:1200px;height:94px;background:linear-gradient(#1fc236,#1a9a2c)}
.tab{position:absolute;top:63px;font-size:14px;font-weight:500;color:var(--white)}
.tab.active{left:364px;top:48px;width:176px;height:46px;background:var(--white);color:var(--ink);border-radius:4px 4px 0 0;display:flex;align-items:center;justify-content:center;font-weight:400}
.card{position:absolute;left:48px;top:188px;width:1102px;height:757px;background:var(--white);box-shadow:0 2px 8px rgba(0,0,0,.18)}
.sidebar{position:absolute;left:34px;top:62px;width:270px;height:624px;background:var(--panel);box-shadow:0 1px 4px rgba(0,0,0,.22)}
.pill{position:absolute;left:37px;width:198px;height:35px;border-radius:18px;font-size:14.5px;display:flex;align-items:center;padding-left:22px;background:var(--panel);color:var(--ink-soft);box-shadow:0 1px 4px rgba(0,0,0,.25)}
.pill.primary{background:linear-gradient(#22bf38,#1a9a2c);color:var(--white);font-size:16px;box-shadow:none}
.pill.dark{background:linear-gradient(#1a9a2c,#137a22);color:var(--white);box-shadow:none}
.pill.field{background:var(--white);font-size:12.5px;border:1px solid #e0e0e0}
.accounts-title{position:absolute;left:0;width:270px;top:256px;text-align:center;font-size:16px;font-weight:500;letter-spacing:.5px}
.side-brand{position:absolute;left:0;width:270px;top:542px;display:flex;justify-content:center;align-items:center;gap:8px;font-size:22px;font-weight:500;white-space:nowrap}
.section-title{position:absolute;left:364px;font-size:20px;font-weight:500}
table{position:absolute;left:363px;border-collapse:collapse;border:1px solid var(--line);font-size:13px}
th{background:linear-gradient(#f3f3f3,#e3e3e3);font-weight:500;font-size:14.5px;height:50px;text-align:left;padding-left:34px;border-left:1px solid var(--line)}
td{height:40px;padding-left:34px;border-left:1px solid var(--line)}
tbody tr:nth-child(4) td{background:var(--stripe)}
tbody tr:nth-child(2) td{box-shadow:inset 0 1px 3px rgba(0,0,0,.06)}
.usd-cell{display:flex;align-items:center;height:40px}
.usd-cell span{width:60px}
.chip{display:inline-block;background:var(--green);color:var(--white);font-size:9.5px;border-radius:10px;padding:2px 14px;font-style:normal}
.tx th{font-size:14px;padding-left:0;text-align:center}
.tx td{padding-left:0;text-align:center}
.tx .chip{padding:2px 19px}
.footer{position:absolute;left:0;width:1200px;top:1006px;text-align:center;font-size:13px;color:var(--ink-soft)}
</style>
</head>
<body>
<header class="topbar">
  <div class="brand"><span class="brand-dot"></span>Orvelle Ledger</div>
  <div class="top-icons">
    <div class="icon-btn"><svg width="14" height="14" viewBox="0 0 14 14"><path d="M7 1a4 4 0 0 1 4 4v4l1.5 1.5h-11L3 9V5a4 4 0 0 1 4-4z" fill="#444"/><circle cx="7" cy="12.5" r="1.4" fill="#444"/></svg></div>
    <div class="icon-btn"><svg width="16" height="16" viewBox="0 0 16 16"><circle cx="8" cy="8" r="6.5" fill="none" stroke="#444" stroke-width="1.6"/><circle cx="8" cy="6.5" r="2.3" fill="#444"/><path d="M3.8 12.5a5 3.5 0 0 1 8.4 0" fill="#444"/></svg></div>
    <div class="icon-btn"><svg width="14" height="14" viewBox="0 0 14 14"><path d="M4 3.5a5 5 0 1 0 6 0" fill="none" stroke="#444" stroke-width="1.6" stroke-linecap="round"/><line x1="7" y1="1" x2="7" y2="7" stroke="#444" stroke-width="1.6" stroke-linecap="round"/></svg></div>
  </div>
</header>
<nav class="navband">
  <div class="tab active">Accounts &amp; Wallet</div>
  <div class="tab" style="left:586px">Get paid</div>
  <div class="tab" style="left:705px">Send &amp; Receive</div>
</nav>
<main class="card">
  <aside class="sidebar">
    <div class="pill primary" style="top:36px">Get Paid</div>
    <div class="pill" style="top:84px">Simulate a Payment</div>
    <div class="pill" style="top:132px">Generate Invoice</div>
    <div class="pill" style="top:180px">Upload Invoice</div>
    <div class="accounts-title">ACCOUNTS</div>
    <div class="pill field" style="top:299px">Name Here (Edit)</div>
    <div class="pill field" style="top:347px">Lable</div>
    <div class="pill dark" style="top:396px">Record New Account</div>
    <div class="side-brand"><span class="brand-dot"></span>Orvelle Ledger</div>
  </aside>

  <h2 class="section-title" style="top:64px">Wallet</h2>
  <table class="wallet" style="top:106px;width:694px">
    <colgroup><col style="width:158px"><col style="width:158px"><col style="width:232px"><col style="width:146px"></colgroup>
    <thead><tr><th>Currency</th><th style="padding-left:40px">Balance</th><th style="padding-left:54px">USD</th><th style="padding-left:30px">More........</th></tr></thead>
    <tbody>
      <tr><td>BTC</td><td style="padding-left:41px">0.000000</td><td style="padding-left:54px"><div class="usd-cell"><span>0.00</span><em class="chip">Topup Wallet</em></div></td><td></td></tr>
      <tr><td>BTCtestnet</td><td style="padding-left:41px">0.000000</td><td style="padding-left:54px"><div class="usd-cell"><span>0.00</span><em class="chip">Topup Wallet</em></div></td><td></td></tr>
      <tr><td>ETH</td><td style="padding-left:41px">0.000000</td><td style="padding-left:54px"><div class="usd-cell"><span>0.00</span><em class="chip">Topup Wallet</em></div></td><td></td></tr>
      <tr><td>LTC</td><td style="padding-left:41px">0.000000</td><td style="padding-left:54px"><div class="usd-cell"><span>0.00</span><em class="chip">Topup Wallet</em></div></td><td></td></tr>
      <tr><td>LTCtestnet</td><td style="padding-left:41px">0.000000</td><td style="padding-left:54px"><div class="usd-cell"><span>0.00</span><em class="chip">Topup Wallet</em></div></td><td></td></tr>
    </tbody>
  </table>

  <h2 class="section-title" style="top:392px">Resent Transactions</h2>
  <table class="tx" style="top:434px;width:694px">
    <colgroup><col style="width:90px"><col style="width:96px"><col style="width:105px"><col style="width:104px"><col style="width:99px"><col style="width:136px"><col style="width:64px"></colgroup>
    <thead><tr><th>Date</th><th>Customer</th><th>Invoice#</th><th>Received</th><th>Amount</th><th>Exchange rate</th><th>Info</th></tr></thead>
    <tbody>
      <tr><td>5/31/2018</td><td>21</td><td>autem</td><td>-</td><td>$20.00</td><td><span class="chip">$15.00</span></td><td>-</td></tr>
      <tr><td>5/31/2018</td><td>32</td><td>autem</td><td>-</td><td>$20.00</td><td><span class="chip">$15.00</span></td><td>-</td></tr>
      <tr><td>5/31/2018</td><td>03</td><td>autem</td><td>-</td><td>$20.00</td><td><span class="chip">$15.00</span></td><td>-</td></tr>
      <tr><td>5/31/2018</td><td>56</td><td>autem</td><td>-</td><td>$20.00</td><td><span class="chip">$15.00</span></td><td>-</td></tr>
      <tr><td>5/31/2018</td><td>03</td><td>autem</td><td>-</td><td>$20.00</td><td><span class="chip">$15.00</span></td><td>-</td></tr>
    </tbody>
  </table>
</main>
<footer class="footer">©2018 OVL, All Rights Reserved.</footer>
</body>
</html>
```